Honey Jar Label Design

I am looking for a fun label design for a 1 lb honey jar.
The company is Rosalind Oakhurst Botanicals, which sells cut flowers and is expanding into honey and eventually other honey products. I've included the design work for the business, and I'd like the honey products to coordinate with them but not necessarily match directly.
Label requirements:
Raw Honey
Rosalind Oakhurst Botanicals
27308 Pebble Hollow Rd
Maple Hollow, KS 66841
NET WT. 16 OZ. (weight info must be in the lower third of the front label and easy to read)
Look and feel
Each slider illustrates characteristics of the customer's brand and the style your logo design should communicate.

```html
<!DOCTYPE html>
<html lang="en">
<head>
<meta charset="utf-8">
<title>Raw Honey Label – Rosalind Oakhurst Botanicals</title>
<link rel="stylesheet" href="https://fonts.googleapis.com/css2?family=Playfair+Display:wght@400;500;600&display=swap">
<style>
  :root {
    --page: #ffffff;
    --label-blush: #e9d7d7;
    --ink-teal: #12292b;
    --band-text: #ffffff;
  }
  * { box-sizing: border-box; margin: 0; padding: 0; }
  html, body {
    width: 1200px;
    height: 1200px;
    overflow: hidden;
    background: var(--page);
  }
  .canvas {
    width: 1200px;
    height: 1200px;
    display: flex;
    align-items: center;
    justify-content: center;
  }
  .honey-label {
    position: relative;
    width: 580px;
    height: 1000px;
    background: var(--label-blush);
    border-radius: 48% 48% 22% 22% / 15% 15% 6% 6%;
    overflow: hidden;
    font-family: "Playfair Display", serif;
    color: var(--ink-teal);
  }
  .floral-pattern {
    position: absolute;
    inset: 0;
    width: 100%;
    height: 100%;
  }
  .label-content {
    position: relative;
    height: 100%;
    display: flex;
    flex-direction: column;
    align-items: center;
  }
  .brand-seal {
    margin-top: 150px;
    width: 360px;
    height: 360px;
    border: 2px solid var(--ink-teal);
    border-radius: 50%;
    display: flex;
    align-items: center;
    justify-content: center;
    text-align: center;
    padding: 0 40px;
  }
  .brand-name {
    font-size: 34px;
    font-weight: 400;
    line-height: 1.3;
    letter-spacing: 0.12em;
    text-transform: uppercase;
  }
  .product-band {
    margin-top: 70px;
    width: 500px;
    height: 64px;
    background: var(--ink-teal);
    color: var(--band-text);
    display: flex;
    align-items: center;
    justify-content: center;
    font-size: 40px;
    font-weight: 500;
    letter-spacing: 0.02em;
  }
  .producer-address {
    margin-top: 70px;
    text-align: center;
    font-size: 21px;
    font-weight: 600;
    font-style: normal;
    line-height: 1.35;
    text-transform: uppercase;
  }
  .net-weight {
    margin-top: 80px;
    font-size: 21px;
    font-weight: 600;
    text-transform: uppercase;
  }
</style>
</head>
<body>
  <main class="canvas">
    <section class="honey-label">
      <svg class="floral-pattern" role="img" aria-label="Faint line-drawn floral pattern across the label background" viewBox="0 0 580 1000" preserveAspectRatio="none">
        <rect width="580" height="1000" fill="var(--label-blush)"/>
      </svg>
      <div class="label-content">
        <div class="brand-seal">
          <p class="brand-name">Rosalind Oakhurst Botanicals</p>
        </div>
        <h1 class="product-band">RAW HONEY</h1>
        <address class="producer-address">
          27308 Pebble Hollow Rd<br>
          Maple Hollow, KS 66841
        </address>
        <p class="net-weight">Net Wt. 16 oz</p>
      </div>
    </section>
  </main>
</body>
</html>
```